New Web Design Project

We need a corporate look website for our Company (Bin Karim for Bright Works) in Oman. We are doing Cabling Supply & Service, BMS SUpply ANd service, Fire and safety supply & Service, Video wall system supply and service, CCTV, Access control, Bio metric system, IT Software and Hardware Supply.
I will give some companies website which are doing the same business, Please refer below.
Cabling service- http://www.veltro-cablenet.com/
BMS , Video wall system, Fire and safety- http://www.fardunsystems.com/
https://www.qvl-tg.com/
https://www.bayrowintegrate.com/

i have uploaded pour company letter head also. Please do the design with the same color in our logo.

```html
<!DOCTYPE html>
<html lang="en">
<head>
<meta charset="utf-8">
<title>Bin Karim for Bright Works</title>
<link rel="stylesheet" href="https://fonts.googleapis.com/css2?family=Montserrat:wght@500;600;700&family=Lato:wght@400;700&display=swap">
<style>
:root{
  --red:#c8282d;
  --red-dark:#a91f24;
  --ink:#222222;
  --text:#6b6b6b;
  --line:#d6d6d6;
  --band:#e7e7e7;
  --footer:#2b2b2b;
  --white:#ffffff;
}
*{box-sizing:border-box;margin:0;padding:0}
html,body{width:1200px;height:3536px;overflow:hidden;background:var(--white)}
body{position:relative;font-family:'Lato',sans-serif;color:var(--text)}
.abs{position:absolute}
.heading{font-family:'Montserrat',sans-serif;font-weight:600;color:var(--ink);letter-spacing:2px;text-transform:uppercase}
.section-title{font-size:21px}
.section-title::after{content:"";display:block;width:44px;height:3px;background:var(--red);margin-top:6px}
.section-title.center::after{margin-left:auto;margin-right:auto}
.btn{display:flex;align-items:center;justify-content:center;font-family:'Montserrat',sans-serif;font-weight:600;text-transform:uppercase;letter-spacing:1px;background:var(--red);color:var(--white)}
.btn-outline{background:var(--white);color:#9a9a9a;border:2px solid var(--line);font-size:11px}

/* hero */
.hero{left:0;top:0;width:1200px;height:636px;background:radial-gradient(ellipse at 85% 30%,#e0506a 0%,#b01c30 35%,#6e0d18 80%,#4a0810 100%)}
.brand{left:75px;top:19px;display:flex;align-items:center;gap:10px}
.brand-mark{width:42px;height:42px;background:var(--red);border:2px solid var(--white)}
.brand-name{font-family:'Montserrat',sans-serif;font-weight:700;color:var(--white);font-size:15px;letter-spacing:1px}
.nav{top:34px;left:0;width:1200px;height:24px}
.nav a{position:absolute;font-family:'Montserrat',sans-serif;font-weight:500;font-size:17px;color:var(--white);text-decoration:none}
.hero-title{left:0;top:270px;width:1200px;text-align:center;font-family:'Montserrat',sans-serif;font-weight:600;font-size:37px;line-height:58px;color:var(--white);letter-spacing:.5px}
.hero-cta{left:488px;top:431px;width:224px;height:62px;font-size:21px;font-weight:500}
.hero-arrow{top:552px;width:32px;height:32px;background:var(--red)}

/* about */
.about-photo{left:73px;top:712px;width:589px;height:426px;background:linear-gradient(180deg,#e9eef2 0%,#c7ccd0 45%,#a77a52 70%,#3d3a3c 100%)}
.about-title{left:712px;top:728px;font-size:21px}
.about-title::after{margin-left:190px}
.about-text{left:712px;top:765px;width:428px;font-size:15.5px;line-height:37px;text-align:justify}
.about-btn{left:712px;top:1070px;width:179px;height:50px;font-size:14px}
.divider{left:0;top:1214px;width:1200px;height:1px;background:#ececec}

/* services */
.services-title{left:0;top:1262px;width:1200px;text-align:center}
.service{top:1336px;width:332px}
.service-photo{width:332px;height:210px}
.service-name{margin-top:36px;font-family:'Montserrat',sans-serif;font-weight:600;font-size:14.5px;color:var(--red);letter-spacing:1px;text-transform:uppercase}
.service-text{margin-top:18px;font-size:12.5px;line-height:19px}
.service .btn{margin-top:18px;width:146px;height:36px;font-size:11px}
.slider-arrow{top:1510px;width:62px;height:62px;border-radius:50%;background:#dd8a8c;display:flex;align-items:center;justify-content:center}

/* projects */
.projects{left:0;top:1855px;width:1200px;height:606px;background:var(--band)}
.projects-title{left:82px;top:1900px}
.project{top:1975px;width:334px;height:335px;background:var(--white);padding:9px}
.project-photo{width:316px;height:229px;position:relative}
.tag{position:absolute;right:10px;top:12px;background:var(--red);color:var(--white);font-family:'Montserrat',sans-serif;font-weight:600;font-size:11px;letter-spacing:1px;padding:4px 9px}
.project-name{margin-top:16px;text-align:center;font-family:'Montserrat',sans-serif;font-weight:600;font-size:19px;color:var(--ink);letter-spacing:.5px}
.project-text{margin:8px auto 0;width:258px;text-align:center;font-size:12.5px;line-height:18px;color:#555}
.project.featured{background:var(--red-dark)}
.project.featured .project-name,.project.featured .project-text{color:var(--white)}
.projects-btn{left:495px;top:2352px;width:224px;height:55px;font-size:14px}

/* partners */
.partners-title{left:73px;top:2506px}
.partner{top:2596px;height:42px;border-radius:6px;background:#d8dde3}
.partner.round{border-radius:50%;background:#2a2a2a}

/* contact */
.map{left:73px;top:2732px;width:504px;height:381px;background:linear-gradient(135deg,#eef0f2 0%,#dfe3e6 55%,#cfe3f2 100%)}
.field{border:2px solid var(--line);background:var(--white);font-size:16px;color:#9a9a9a;padding:14px 20px}
.submit{left:698px;top:3050px;width:224px;height:63px;font-size:19px;font-weight:500}

/* footer */
.footer{left:0;top:3184px;width:1200px;height:352px;background:var(--footer)}
.footer-mark{left:118px;top:3279px;width:115px;height:108px;background:var(--red);border:3px solid var(--white)}
.footer-name{left:98px;top:3400px;width:155px;text-align:center;font-family:'Montserrat',sans-serif;font-weight:500;color:var(--white);font-size:18px}
.col-title{top:3250px;font-family:'Montserrat',sans-serif;font-weight:500;font-size:21px;color:var(--red);text-transform:uppercase;letter-spacing:.5px}
.col-list{top:3298px;list-style:none;font-size:17px;color:#e6e6e6;line-height:37.5px}
.address{left:896px;top:3296px;font-size:14.5px;line-height:21px;color:#e6e6e6}
.footer-rule{left:0;top:3467px;width:1200px;height:1px;background:#444}
.social{top:3486px;width:32px;height:32px;border-radius:50%;background:var(--red)}
</style>
</head>
<body>

<!-- header / hero -->
<div class="abs hero" role="img" aria-label="Close-up photo of a red LED video wall with glowing pink dots"></div>
<div class="abs brand"><span class="brand-mark"></span><span class="brand-name">BIN KARIM</span></div>
<nav class="abs nav">
  <a style="left:667px">HOME</a>
  <a style="left:768px">ABOUT</a>
  <a style="left:877px">SERVICES</a>
  <a style="left:1009px">CONTACT</a>
</nav>
<h1 class="abs hero-title">Lorem ipsum dolor sit amet, consectetur<br>adipiscing elit. Aenean mi</h1>
<div class="abs btn hero-cta">Explore</div>
<div class="abs hero-arrow" style="left:552px"><svg width="32" height="32" viewBox="0 0 32 32"><path d="M19 10l-6 6 6 6" fill="none" stroke="#fff" stroke-width="3"/></svg></div>
<div class="abs hero-arrow" style="left:604px"><svg width="32" height="32" viewBox="0 0 32 32"><path d="M13 10l6 6-6 6" fill="none" stroke="#fff" stroke-width="3"/></svg></div>

<!-- about -->
<div class="abs about-photo" role="img" aria-label="Photo of a team meeting around a long table in a bright conference room"></div>
<h2 class="abs heading about-title section-title">About Bin Karim</h2>
<p class="abs about-text">Lorem ipsum dolor sit amet, consectetur adipiscing elit. Donec et velit orci. Duis felis massa, tempor vel tempor eu, euismod vitae lorem. Maecenas imperdiet tellus sapien, eget eleifend eros mattis id. Pellentesque lacus dolor, sollicitudin eget malesuada sed, ultricies id purus. Suspendisse ac sapien sapien. Aenean odio lectus, pulvinar ut eros at, tempor efficitur purus. Cras feugiat libero velit, at</p>
<div class="abs btn about-btn">Read More</div>
<div class="abs divider"></div>

<!-- services -->
<h2 class="abs heading services-title section-title center">Our Services</h2>
<div class="abs service" style="left:73px">
  <div class="service-photo" role="img" aria-label="Photo of a hand working on colourful network cabling in a panel" style="background:linear-gradient(135deg,#d9dcd6 0%,#9aa59a 40%,#6b7a6f 100%)"></div>
  <div class="service-name">Cabling Supply &amp; Service</div>
  <p class="service-text">Lorem ipsum dolor sit amet, consectetur adipiscing elit. Duis lectus tellus, rutrum vel feugiat ut, convallis sit amet justo. Proin placerat diam id gravida</p>
  <div class="btn btn-outline">Read More</div>
</div>
<div class="abs service" style="left:434px">
  <div class="service-photo" role="img" aria-label="Photo of a technician with a laptop in a blue-lit server room" style="background:linear-gradient(135deg,#0e1c3a 0%,#1f3f7a 50%,#0a1224 100%)"></div>
  <div class="service-name">IT Software &amp; Hardware Supply</div>
  <p class="service-text">Lorem ipsum dolor sit amet, consectetur adipiscing elit. Duis lectus tellus, rutrum vel feugiat ut, convallis sit amet justo. Proin placerat diam id gravida</p>
  <div class="btn">Read More</div>
</div>
<div class="abs service" style="left:799px">
  <div class="service-photo" role="img" aria-label="Photo of firefighters spraying water at a blaze" style="background:linear-gradient(135deg,#2a1a12 0%,#a4471c 50%,#e0a04a 100%)"></div>
  <div class="service-name">Fire and Safety Supply &amp; Service</div>
  <p class="service-text">Lorem ipsum dolor sit amet, consectetur adipiscing elit. Duis lectus tellus, rutrum vel feugiat ut, convallis sit amet justo. Proin placerat diam id gravida</p>
  <div class="btn btn-outline">Read More</div>
</div>
<div class="abs slider-arrow" style="left:40px"><svg width="24" height="24" viewBox="0 0 24 24"><path d="M15 5l-7 7 7 7" fill="none" stroke="#fff" stroke-width="3"/></svg></div>
<div class="abs slider-arrow" style="left:1096px"><svg width="24" height="24" viewBox="0 0 24 24"><path d="M9 5l7 7-7 7" fill="none" stroke="#fff" stroke-width="3"/></svg></div>

<!-- projects -->
<div class="abs projects"></div>
<h2 class="abs heading projects-title section-title">Our Projects</h2>
<div class="abs project" style="left:78px">
  <div class="project-photo" role="img" aria-label="Photo of a keypad access control unit on a wall" style="background:linear-gradient(135deg,#8e8f93 0%,#4d5a78 55%,#26282c 100%)"><span class="tag">CURRENT</span></div>
  <div class="project-name">LOREM IPSUM DOLOR</div>
  <p class="project-text">Lorem ipsum dolor sit amet, consectetur adipiscing elit. Aenean mi augue, fermen-</p>
</div>
<div class="abs project" style="left:438px">
  <div class="project-photo" role="img" aria-label="Photo of a red fire hose reel and extinguisher on a wooden wall" style="background:linear-gradient(135deg,#a37a58 0%,#8a6446 50%,#b83a2e 100%)"><span class="tag">COMPLETE</span></div>
  <div class="project-name">LOREM IPSUM DOLOR</div>
  <p class="project-text">Lorem ipsum dolor sit amet, consectetur adipiscing elit. Aenean mi augue, fermen-</p>
</div>
<div class="abs project featured" style="left:785px">
  <div class="project-photo" role="img" aria-label="Black and white photo of a computer lab with rows of workstations" style="background:linear-gradient(135deg,#d6d6d6 0%,#8e8e8e 55%,#3e3e3e 100%)"><span class="tag">CURRENT</span></div>
  <div class="project-name">LOREM IPSUM DOLOR</div>
  <p class="project-text">Lorem ipsum dolor sit amet, consectetur adipiscing elit. Aenean mi augue, fermen-</p>
</div>
<div class="abs btn projects-btn">More Projects</div>

<!-- partners -->
<h2 class="abs heading partners-title section-title">Our Partners</h2>
<div class="abs partner" style="left:75px;width:134px"></div>
<div class="abs partner round" style="left:297px;top:2585px;width:60px;height:60px"></div>
<div class="abs partner round" style="left:483px;top:2585px;width:60px;height:60px"></div>
<div class="abs partner" style="left:618px;width:136px"></div>
<div class="abs partner round" style="left:838px;top:2585px;width:60px;height:60px"></div>
<div class="abs partner" style="left:993px;width:134px"></div>

<!-- contact -->
<div class="abs map" role="img" aria-label="Street map with a location pin marking the office in Ruwi"></div>
<div class="abs field" style="left:698px;top:2732px;width:429px;height:64px">Full Name</div>
<div class="abs field" style="left:698px;top:2824px;width:200px;height:61px">Email</div>
<div class="abs field" style="left:924px;top:2824px;width:203px;height:61px">Phone</div>
<div class="abs field" style="left:698px;top:2913px;width:429px;height:109px">Message</div>
<div class="abs btn submit">Submit</div>

<!-- footer -->
<footer class="abs footer"></footer>
<div class="abs footer-mark"></div>
<div class="abs footer-name">BIN KARIM</div>
<div class="abs col-title" style="left:441px">Quick Links</div>
<ul class="abs col-list" style="left:446px"><li>Home</li><li>About Us</li><li>Our Services</li><li>Our Blogs</li></ul>
<div class="abs col-title" style="left:679px">Resources</div>
<ul class="abs col-list" style="left:684px"><li>Support</li><li>Why Us?</li><li>Privacy</li><li>Terms</li></ul>
<div class="abs col-title" style="left:896px">Contact Us</div>
<p class="abs address">Unit 12, 9 Qurum Heights<br>Road<br>Muscat<br>Oman<br><span style="display:block;margin-top:8px">hello@binkarimworks.com</span></p>
<div class="abs footer-rule"></div>
<div class="abs social" style="left:889px"></div>
<div class="abs social" style="left:943px"></div>
<div class="abs social" style="left:1000px"></div>
<div class="abs social" style="left:1056px"></div>

</body>
</html>
```